Real Estate For Sale Flyer Design Project

BrightOak Group of Realtors. We sell homes but want a more modern feel than the standard boring real estate flyers of the past. We want 8.5x11 flyers

Target Market(s)

mid level income home owners

Industry/Entity Type

Real Estate

Requirements
Must have
• fun

```html
<!DOCTYPE html>
<html lang="en">
<head>
<meta charset="utf-8">
<title>BrightOak Team – For Sale Flyer</title>
<link href="https://fonts.googleapis.com/css2?family=Montserrat:wght@600;700;800;900&family=Open+Sans:wght@400;600&display=swap" rel="stylesheet">
<style>
  :root{
    --purple:#6a1b9a;
    --purple-light:#8e3cc0;
    --black:#0d0d0d;
    --white:#ffffff;
    --body-text:#333333;
    --sky-top:#9fb8d6;
    --sky-bottom:#d8e2ee;
    --house-tone:#8a8f9c;
  }
  *{margin:0;padding:0;box-sizing:border-box}
  html,body{width:900px;height:1200px;overflow:hidden;background:#e9e6e1}
  .flyer{
    position:relative;width:900px;height:1200px;overflow:hidden;
    background:var(--black);font-family:"Open Sans",sans-serif;
  }
  /* header */
  .brand{position:absolute;left:40px;top:28px;display:flex;align-items:center;gap:14px}
  .brand-dot{width:62px;height:62px;border-radius:50%;background:var(--purple)}
  .brand-name{font-family:"Montserrat",sans-serif;font-weight:800;font-size:34px;color:var(--purple-light);line-height:1}
  .brand-tagline{font-size:12px;color:var(--white);margin-top:6px;letter-spacing:.3px}
  /* hero */
  .hero-photo{
    position:absolute;left:0;top:115px;width:900px;height:560px;
    background:linear-gradient(180deg,var(--sky-top) 0%,var(--sky-bottom) 45%,var(--house-tone) 75%,#4d5560 100%);
  }
  .hero-shapes{position:absolute;left:0;top:100px}
  .offer{position:absolute;left:55px;top:430px;width:250px;height:250px}
  .offer-text{
    position:absolute;inset:0;display:flex;flex-direction:column;align-items:center;justify-content:center;
    font-family:"Montserrat",sans-serif;color:var(--white);text-align:center;
  }
  .offer-label{font-weight:900;font-size:36px;line-height:1.05}
  .offer-price{font-weight:800;font-size:40px;margin-top:6px;letter-spacing:.5px}
  .headline{
    position:absolute;right:40px;top:600px;text-align:right;
    font-family:"Montserrat",sans-serif;font-weight:900;color:var(--white);
    font-size:44px;line-height:1.05;
  }
  /* info */
  .info{position:absolute;left:0;top:715px;width:900px;height:285px;background:var(--white)}
  .tab{
    display:inline-block;background:var(--purple);color:var(--white);
    font-family:"Montserrat",sans-serif;font-weight:700;font-size:16px;
    padding:7px 26px;border-radius:3px;
  }
  .about{position:absolute;left:40px;top:22px;width:380px}
  .about .tab{margin-left:80px}
  .about p{margin-top:14px;font-size:14.5px;line-height:1.4;color:var(--body-text);text-align:justify}
  .services{position:absolute;left:460px;top:22px;width:410px}
  .services .tab{margin-left:90px}
  .service-list{display:grid;grid-template-columns:1fr 1fr;column-gap:20px;margin-top:18px;list-style:none}
  .service-list li{
    position:relative;padding-left:16px;font-size:12.5px;color:var(--purple);
    line-height:1.3;margin-bottom:12px;font-weight:600;
  }
  .service-list li::before{
    content:"";position:absolute;left:0;top:5px;width:7px;height:7px;border-radius:50%;background:var(--purple);
  }
  /* footer */
  .contacts{position:absolute;left:40px;top:1040px;list-style:none}
  .contacts li{display:flex;align-items:center;gap:16px;color:var(--white);font-size:17px;margin-bottom:18px}
  .contact-icon{width:34px;height:34px;border-radius:50%;background:var(--purple);display:flex;align-items:center;justify-content:center}
  .listing-photo{
    position:absolute;left:545px;top:890px;width:355px;height:310px;
    background:linear-gradient(180deg,#c9d6e4 0%,#b4553f 38%,#9a6a52 70%,#5c6b46 100%);
  }
</style>
</head>
<body>
<div class="flyer">
  <header class="brand">
    <div class="brand-dot"></div>
    <div>
      <div class="brand-name">BrightOak Team</div>
      <div class="brand-tagline">BrightOak Group of Realtors</div>
    </div>
  </header>

  <div class="hero-photo" role="img" aria-label="Photo of a large two-storey grey family home with a double garage at dusk"></div>

  <svg class="hero-shapes" width="900" height="620" viewBox="0 0 900 620" aria-hidden="true">
    <polygon points="520,15 900,15 900,90" fill="var(--purple)"/>
    <polygon points="0,540 900,360 900,620 0,620" fill="var(--white)"/>
    <polygon points="290,520 900,400 900,604 290,604" fill="var(--purple)"/>
    <polygon points="0,604 900,604 900,620 0,620" fill="var(--white)"/>
  </svg>

  <div class="offer">
    <svg width="250" height="250" viewBox="0 0 240 240" aria-hidden="true">
      <polygon fill="var(--black)" stroke="var(--white)" stroke-width="3"
        points="238,120 216.6,145.9 222.2,179 190.7,190.7 179,222.2 145.9,216.6 120,238 94.1,216.6 61,222.2 49.3,190.7 17.8,179 23.4,145.9 2,120 23.4,94.1 17.8,61 49.3,49.3 61,17.8 94.1,23.4 120,2 145.9,23.4 179,17.8 190.7,49.3 222.2,61 216.6,94.1"/>
    </svg>
    <div class="offer-text">
      <div class="offer-label">OFFER<br>AT</div>
      <div class="offer-price">$012121</div>
    </div>
  </div>

  <h1 class="headline">LOREM IPSUM<br>DOLOR SIT AMET</h1>

  <section class="info">
    <div class="about">
      <span class="tab">ABOUT US</span>
      <p>Eos stet suscipit no, nam et delicata accusamus. Ne has adhuc inermis, tota illum interpretaris cum eu. Pri facilisi qualisque prodesset an. Vix at voluptaria voluptatibus necessitatibus. Possit indoctum suscipiantur at cum, in dicit veris postulant duo, eu sed agam antiopam consetetur. Cu vim dolorem debitis graecis.</p>
    </div>
    <div class="services">
      <span class="tab">OUR SERVICE</span>
      <ul class="service-list">
        <li>Home buying guidance</li>
        <li>Relocation support</li>
        <li>Free market appraisals</li>
        <li>Investment advice</li>
        <li>Listing and staging</li>
        <li>Rental management</li>
        <li>Mortgage referrals</li>
        <li>Open house events</li>
      </ul>
    </div>
  </section>

  <ul class="contacts">
    <li>
      <span class="contact-icon"><svg width="18" height="18" viewBox="0 0 24 24"><path fill="#fff" d="M6.6 10.8a15.1 15.1 0 0 0 6.6 6.6l2.2-2.2a1 1 0 0 1 1-.25 11.4 11.4 0 0 0 3.6.57 1 1 0 0 1 1 1V20a1 1 0 0 1-1 1A17 17 0 0 1 3 4a1 1 0 0 1 1-1h3.5a1 1 0 0 1 1 1c0 1.25.2 2.45.57 3.57a1 1 0 0 1-.25 1z"/></svg></span>
      0123456789
    </li>
    <li>
      <span class="contact-icon"><svg width="18" height="18" viewBox="0 0 24 24"><rect x="3" y="6" width="18" height="12" rx="1.5" fill="#fff"/><path d="M3.5 7 12 13l8.5-6" stroke="var(--purple)" stroke-width="1.8" fill="none"/></svg></span>
      www.company@mail.com
    </li>
    <li>
      <span class="contact-icon"><svg width="18" height="18" viewBox="0 0 24 24" fill="none" stroke="#fff" stroke-width="1.8"><circle cx="12" cy="12" r="9"/><ellipse cx="12" cy="12" rx="4" ry="9"/><path d="M3 12h18"/></svg></span>
      www.companywebsite.com
    </li>
  </ul>

  <div class="listing-photo" role="img" aria-label="Photo of a red-roofed brick house with solar panels and a front lawn"></div>
</div>
</body>
</html>
```